poster for a contemporary music concert series

Our association is hosting a series of contemporary music concerts.
The setup is classical - from chamber music trio, midsized ensemble until orchestra.
context/topic:
Every ensemble for contemporary music in the city is playing one concert in the series. We have one common topic each year. This year’s topic is about a composition idea  called "Tonverwebung". Each concert has one assigned student who is responsible to write a new piece that will be performed. This piece uses material generated by the LAST concert of the series. The used material can be anything (the score, the recording, a video recording, ...).
task:
We need a poster that will be printed in A3 format throughout the city before every concert. The poster must contain all the information of the concert series and must have places for the individual names of the performing ensemble/title/program.
The poster is used six times for six different ensembles. Although it is ONE series, we would like to have it easily visible that there are different concerts. We think the easiest way is to use complete different colors for background to distinguish the different ensembles/program titels from each other.
Things to be included on the poster:
- the title of the concert series is "de:turns".
- the concert place is "Lindenhof-Halle Dresden, großer Saal"
- the price is  "15€ normal / 10€ ermäßigt"
- the logo of TonGeflecht-Dresden can be used in any of the colours provided - somewhere should be mentioned, that this concert series is a cooperation "de:turns – Eine Konzertreihe von TonGeflecht-Dresden in Kooperation mit dem Lindenhof-Halle Dresden"
- the logo of the museum where we play is included and should be used
- the pdf shows examples of previous years
- there must be one bottom line in white for the needed logos of the funding partners. The funding partners are different from each concert, I included here three of them for visual purposes

Updates
- please don't use parts of the old posters. We have complete new posters for every year. The rectangle and the "Intelligenz" was part of last year's design.
- the music that is coming is not classical in a way that any instrument pictures would help to promote it. It's composed today, so very modern and often with use of electronics (de:turns is often inspired composers to a  kind of feedback, loop, variance, or ... of the previous material)

Target Market(s)
concert audience, young people
Industry/Entity Type
contemporary (classical) music
Requirements
Must have
- things mentioned in the brief description

Nice to have
- a visual look that shows that it is about contemporary music. IF there is any idea how to visualize the IDEA of the concert series this year (taking material from previous concerts and recompose it to the next ensemble) - this would be WONDERFUL. not necessary a copy, nor fake - just a reference to the old ones - and so on :-)

Should not have
- symbolic images/clipart/anything "musically" --> more avantgarde or abstract style is better

```html
<!DOCTYPE html>
<html lang="de">
<head>
<meta charset="utf-8">
<title>de:turns – Porträts</title>
<link rel="stylesheet" href="https://fonts.googleapis.com/css2?family=Montserrat:wght@500;600;700;800&display=swap">
<style>
  :root {
    --bg: #262626;
    --yellow: #f7c20f;
    --yellow-deep: #e9a90a;
    --white: #ffffff;
    --ink: #1e1e1e;
    --partner: #c9c9c9;
  }
  * { margin: 0; padding: 0; box-sizing: border-box; }
  html, body { width: 705px; height: 1200px; overflow: hidden; background: var(--bg); }
  body { font-family: "Montserrat", Arial, sans-serif; color: var(--white); }
  .poster { position: relative; width: 705px; height: 1200px; background: var(--bg); overflow: hidden; }

  .series-note { position: absolute; left: 30px; top: 30px; font-size: 9.5px; font-weight: 700; line-height: 1.3; }
  .org-marks { position: absolute; right: 30px; top: 28px; display: flex; gap: 22px; align-items: center; }
  .org-mark { display: flex; align-items: center; gap: 6px; font-size: 10px; font-weight: 700; line-height: 1.1; }
  .org-mark .dot { width: 22px; height: 22px; border-radius: 50%; background: var(--white); }

  .ensemble { position: absolute; top: 127px; width: 100%; text-align: center; color: var(--yellow); font-size: 20px; font-weight: 700; }
  .title { position: absolute; top: 148px; width: 100%; text-align: center; font-size: 94px; font-weight: 600; line-height: 1; }
  .when-where { position: absolute; top: 252px; width: 100%; text-align: center; color: var(--yellow); font-size: 17px; font-weight: 700; line-height: 1.35; }

  .scroll-art { position: absolute; left: 318px; top: 325px; width: 70px; height: 115px; background: radial-gradient(ellipse at center, #8a8a8a 0%, #4a4a4a 60%, transparent 75%); }
  .beam-art { position: absolute; left: 192px; top: 430px; width: 296px; height: 580px; background: linear-gradient(180deg, var(--yellow) 0%, var(--yellow-deep) 100%); clip-path: polygon(48.6% 0, 60.1% 0, 100% 100%, 0 100%); }

  .series-vertical { position: absolute; left: 352px; top: 728px; transform: translate(-50%, -50%) rotate(-90deg); font-size: 56px; font-weight: 700; color: var(--white); white-space: nowrap; }

  .program { position: absolute; font-size: 14px; font-weight: 700; line-height: 1.4; }
  .program .name { color: var(--yellow); font-size: 16px; font-weight: 800; line-height: 1.3; }
  .program.left { left: 30px; width: 230px; }
  .program.right { right: 32px; width: 190px; text-align: right; }

  .players-art { position: absolute; left: 225px; top: 925px; width: 250px; height: 85px; background: linear-gradient(180deg, #3a3a3a 0%, #111 100%); }
  .floor-art { position: absolute; left: 0; top: 1008px; width: 705px; height: 125px; background: linear-gradient(180deg, #1c1c1c 0%, #5a5a5a 100%); }

  .tickets { position: absolute; left: 155px; top: 1040px; width: 390px; height: 70px; background: var(--yellow); border-radius: 12px; color: var(--ink); text-align: center; font-size: 12.5px; font-weight: 700; line-height: 1.35; padding-top: 7px; }
  .tickets .url { display: block; margin: 5px auto 0; width: 320px; height: 22px; background: var(--white); border-radius: 11px; font-size: 13px; line-height: 22px; }

  .partners { position: absolute; left: 0; top: 1133px; width: 705px; height: 67px; background: var(--white); display: flex; align-items: center; justify-content: space-around; padding: 0 40px; }
  .partner { background: var(--partner); height: 22px; }
  .partner.round { width: 30px; height: 30px; border-radius: 50%; }
</style>
</head>
<body>
<main class="poster">
  <p class="series-note">de:turns – Eine Konzertreihe von TonGeflecht-Dresden<br>in Kooperation mit dem Lindenhof-Halle Dresden</p>
  <div class="org-marks">
    <div class="org-mark"><span class="dot"></span>TonGeflecht<br>Dresden</div>
    <div class="org-mark"><span class="dot"></span>Lindenhof-Halle<br>Dresden</div>
  </div>

  <p class="ensemble">Kammerwerk Dresden</p>
  <h1 class="title">Porträts</h1>
  <p class="when-where">Mo 22. NOV 2021 _ 19:30 Uhr<br>Lindenhof-Halle Dresden, großer Saal</p>

  <div class="scroll-art" role="img" aria-label="Abstrakte Bildfläche am oberen Ende des Lichtkegels"></div>
  <div class="beam-art" role="img" aria-label="Gelber Lichtkegel als zentrale Bildfläche"></div>

  <div class="series-vertical">de:turns</div>

  <section class="program left" style="top:490px">
    <div class="name">TOBIAS WARNKE</div>Flötenkonzert – Vor Der Verdunklung (UA)
  </section>
  <section class="program left" style="top:587px">
    <div class="name">FERENC HALMOS</div>Bläserquintett OP. 2
  </section>
  <section class="program left" style="top:682px">
    <div class="name">MARTA EICHHORN</div>Violinkonzert Zur Osterzeit (UA)
  </section>

  <section class="program right" style="top:490px">
    <div class="name">JONAS PETER REHFELD</div>Leitung
  </section>
  <section class="program right" style="top:587px">
    <div class="name">INA-SOPHIE KALLWEIT</div>Violine
  </section>
  <section class="program right" style="top:682px">
    <div class="name">HENRIK SAALBACH</div>Flöte
  </section>

  <div class="players-art" role="img" aria-label="Silhouetten eines Ensembles mit Dirigent"></div>
  <div class="floor-art" role="img" aria-label="Dunkler perspektivischer Boden"></div>

  <div class="tickets">
    Tickets: 15 € / 10 € erm. unter lindenhof-halle.de<br>
    und an der Abendkasse Einführungsgespräch: 18:45 Uhr
    <span class="url">https://www.tongeflecht-dresden.de/</span>
  </div>

  <footer class="partners" aria-label="Förderpartner">
    <span class="partner" style="width:60px"></span>
    <span class="partner" style="width:90px"></span>
    <span class="partner" style="width:70px"></span>
    <span class="partner" style="width:60px"></span>
    <span class="partner" style="width:40px"></span>
    <span class="partner round"></span>
    <span class="partner" style="width:80px"></span>
  </footer>
</main>
</body>
</html>
```